Cutting Edge Software Company

My software runs on an older computer platform called an KX720. The software that runs on an KX720 is typically referred to as 'green screen' (green text on a black screen). My software runs in a browser and has all of the bells and whistles available in an HTML solution. I relate the difference as the Knight of Rell before and after the twister. I would like the motto 'The Ledger Crafts Company' underlined or highlighted in some way since that is the name of our product. If possible I would like the first letters of the company name (MVS) to subliminally stand out.
hospitality companies
Software
Meadow and Vale Systems
The Ledger Crafts Company
4872 SE 19th Avenue
Coral Springs

```html
<!DOCTYPE html>
<html lang="en">
<head>
<meta charset="UTF-8">
<title>Meadow and Vale Systems – Business Card</title>
<link rel="stylesheet" href="https://fonts.googleapis.com/css2?family=Michroma&family=Montserrat:wght@400;500;600&display=swap">
<style>
  :root {
    --stage: #eef1f4;
    --card-light: #ffffff;
    --card-grey: #dcdcdc;
    --band-deep: #19a3e3;
    --band-light: #5fc9f5;
    --brand-blue: #1b8fd0;
    --ink-dark: #3a3a3a;
    --ink-mid: #6d6d6d;
    --white: #ffffff;
  }
  * { box-sizing: border-box; margin: 0; padding: 0; }
  html, body {
    width: 1200px; height: 906px; overflow: hidden;
    background: var(--stage);
  }
  .canvas { position: relative; width: 1200px; height: 906px; }

  .card {
    position: absolute;
    width: 640px; height: 366px;
    overflow: hidden;
    background: linear-gradient(160deg, var(--card-light) 0%, #f1f1f1 45%, var(--card-grey) 100%);
    box-shadow: 0 10px 28px rgba(0,0,0,0.18);
  }
  .card--front { left: 60px; top: 60px; }
  .card--back { left: 500px; top: 480px; }

  .band {
    position: absolute; left: 0; right: 0; bottom: 0;
    background: linear-gradient(180deg, var(--band-light) 0%, var(--band-deep) 100%);
  }
  .card--front .band { height: 120px; }
  .card--back .band { height: 170px; }

  .brand { position: absolute; text-align: center; }
  .brand__name {
    font-family: "Michroma", sans-serif;
    font-size: 21px; letter-spacing: 1px;
    font-variant-caps: small-caps;
    color: var(--brand-blue);
    white-space: nowrap;
  }
  .brand__tagline {
    display: inline-block;
    font-family: "Michroma", sans-serif;
    font-size: 10.5px; letter-spacing: 2.4px;
    color: var(--ink-mid);
    text-transform: uppercase;
    margin-top: 8px;
    padding-bottom: 4px;
    border-bottom: 2px solid var(--band-deep);
    white-space: nowrap;
  }
  .card--front .brand { left: 0; right: 0; top: 86px; }
  .card--back .brand { left: 40px; top: 104px; text-align: left; }
  .card--back .brand__name { font-size: 18px; }
  .card--back .brand__tagline { font-size: 9px; letter-spacing: 2px; }

  .website-line {
    position: absolute; right: 40px; bottom: 38px;
    font-family: "Montserrat", sans-serif; font-weight: 500;
    font-size: 19px; letter-spacing: 0.5px;
    color: var(--white);
  }

  .person { position: absolute; right: 40px; top: 40px; text-align: left; }
  .person__name {
    font-family: "Michroma", sans-serif;
    font-size: 20px; letter-spacing: 2px;
    color: var(--brand-blue);
  }
  .person__title {
    font-family: "Montserrat", sans-serif; font-weight: 600;
    font-size: 11px; letter-spacing: 2px;
    color: var(--ink-dark);
    margin-top: 6px;
    text-transform: uppercase;
  }

  .contacts {
    position: absolute; left: 0; right: 0; bottom: 0; height: 170px;
    display: flex; justify-content: space-between; align-items: flex-start;
    padding: 34px 34px 0 40px;
  }
  .contact { display: flex; flex-direction: column; align-items: center; }
  .contact__icon {
    width: 46px; height: 46px; border-radius: 50%;
    background: var(--white);
    display: flex; align-items: center; justify-content: center;
    margin-bottom: 12px;
  }
  .contact__icon svg { width: 26px; height: 26px; }
  .contact__text {
    font-family: "Montserrat", sans-serif; font-weight: 500;
    font-size: 12.5px; line-height: 1.45;
    color: var(--white); text-align: center;
    letter-spacing: 0.3px;
  }
</style>
</head>
<body>
<main class="canvas">

  <section class="card card--front" aria-label="Card front">
    <div class="brand">
      <p class="brand__name">Meadow and Vale Systems</p>
      <p class="brand__tagline">The Ledger Crafts Company</p>
    </div>
    <div class="band">
      <p class="website-line">www.meadowvalesys.com</p>
    </div>
  </section>

  <section class="card card--back" aria-label="Card back">
    <div class="person">
      <p class="person__name">MARLA QUINT</p>
      <p class="person__title">General Manager</p>
    </div>
    <div class="brand">
      <p class="brand__name">Meadow and Vale Systems</p>
      <p class="brand__tagline">The Ledger Crafts Company</p>
    </div>
    <div class="band"></div>
    <div class="contacts">
      <div class="contact">
        <span class="contact__icon">
          <svg viewBox="0 0 24 24" aria-hidden="true">
            <path d="M3 12 L12 4 L21 12" fill="none" stroke="var(--band-deep)" stroke-width="2.2" stroke-linejoin="round"/>
            <path d="M6 11 V20 H10 V15 H14 V20 H18 V11" fill="var(--band-deep)"/>
          </svg>
        </span>
        <p class="contact__text">4872 SE 19th Avenue<br>Coral Springs</p>
      </div>
      <div class="contact">
        <span class="contact__icon">
          <svg viewBox="0 0 24 24" aria-hidden="true">
            <path d="M5 9 C5 6 7 5 12 5 C17 5 19 6 19 9 L16 10 L15 8 H9 L8 10 Z" fill="var(--band-deep)"/>
            <path d="M7 12 H17 L19 19 H5 Z" fill="var(--band-deep)"/>
            <circle cx="12" cy="15.5" r="1.8" fill="var(--white)"/>
          </svg>
        </span>
        <p class="contact__text">014 552 0937<br>014 552 0938</p>
      </div>
      <div class="contact">
        <span class="contact__icon">
          <svg viewBox="0 0 24 24" aria-hidden="true">
            <g fill="none" stroke="var(--band-deep)" stroke-width="1.8">
              <circle cx="12" cy="12" r="8.5"/>
              <ellipse cx="12" cy="12" rx="3.8" ry="8.5"/>
              <line x1="3.5" y1="12" x2="20.5" y2="12"/>
              <line x1="12" y1="3.5" x2="12" y2="20.5"/>
            </g>
          </svg>
        </span>
        <p class="contact__text">hello@mvsmail.com<br>www.meadowvalesys.com</p>
      </div>
    </div>
  </section>

</main>
</body>
</html>
```